Silverleaf upkeep services strata flyer

Looking for a flyer that will grab peoples attention also need to include some kind off promotional offer on there so they will hold onto the flyer . Would like approximateley 4 pictures of appartment blocks. Would like to include the following services. Building management Common area cleaning ,window cleaning, lawn mowing, gardening , pressure cleaning, carpet cleaning, bin cleaning. Handy man services.

Target Market(s)

appartment blocks/strata managers

Industry/Entity Type

Pressure Cleaning

Font styles to use
Serif

Colors
0355a3
ceddec
ec2027

Requirements
Must have
• company logo & colors contact details email: Info@silverleafupkeepservices.com.au
• Phone: 0438507721 website silverleafupkeepservices.com.au

```html
<!DOCTYPE html>
<html lang="en">
<head>
<meta charset="utf-8">
<title>Silverleaf Upkeep Services – Strata Flyer</title>
<link rel="stylesheet" href="https://fonts.googleapis.com/css2?family=Oswald:wght@500;600&family=Lato:wght@700&display=swap">
<style>
  :root{
    --red:#ec2027;
    --blue:#0355a3;
    --mist:#ceddec;
    --ink:#2b2b2b;
    --maroon:#4a1417;
    --white:#ffffff;
    --paper:#f1f2f4;
  }
  html,body{margin:0;padding:0;overflow:hidden;background:#e6e6e6;}
  .flyer{position:relative;width:920px;height:1200px;overflow:hidden;background:var(--paper);}
  .photo{position:absolute;}
  .photo--hero{left:0;top:40px;width:920px;height:680px;
    background:linear-gradient(180deg,#9cc3e6 0%,#e9ecef 30%,#d9dde0 55%,#7fa05a 72%,#5f8a3a 100%);}
  .photo--block-a{left:511px;top:540px;width:409px;height:184px;
    background:linear-gradient(135deg,#7a8da6 0%,#eef1f4 45%,#4d5560 100%);}
  .photo--block-b{left:511px;top:728px;width:409px;height:256px;
    background:linear-gradient(180deg,#6fa3de 0%,#d9d2c6 45%,#a49a8a 75%,#6e8b4e 100%);}
  .photo--block-c{left:511px;top:988px;width:409px;height:212px;
    background:linear-gradient(180deg,#7fb0e0 0%,#ece9e4 40%,#9a6e5c 65%,#4f7a3a 100%);}
  .shapes{position:absolute;left:0;top:0;width:920px;height:1200px;}
  .website{position:absolute;right:24px;top:9px;margin:0;color:var(--white);
    font:700 20px/1.2 'Lato',sans-serif;}
  .brand{position:absolute;left:38px;top:92px;display:flex;align-items:center;gap:16px;}
  .brand__dot{width:58px;height:58px;border-radius:50%;background:var(--white);flex:none;}
  .brand__name{margin:0;color:var(--white);font:600 34px/1.05 'Oswald',sans-serif;text-transform:uppercase;}
  .banner-title{position:absolute;left:178px;top:726px;margin:0;color:var(--white);
    font:600 27px/40px 'Oswald',sans-serif;text-transform:uppercase;white-space:nowrap;}
  .banner-title span{color:var(--maroon);}
  .services{position:absolute;top:820px;margin:0;padding:0;list-style:none;
    font:700 18.5px/27px 'Lato',sans-serif;color:var(--ink);text-align:right;}
  .services li::after{content:"";display:inline-block;width:6px;height:6px;border-radius:50%;
    background:var(--red);margin-left:12px;vertical-align:middle;}
  .services--left{right:672px;}
  .services--right{right:459px;}
  .offer{position:absolute;left:44px;width:430px;top:960px;margin:0;text-align:center;
    font:700 16px/24px 'Lato',sans-serif;color:var(--red);}
  .tagline{position:absolute;left:44px;width:430px;top:1002px;margin:0;text-align:center;
    font:600 35px/1.1 'Oswald',sans-serif;color:var(--blue);text-transform:uppercase;}
  .tagline span{color:var(--red);}
  .call{position:absolute;left:0;width:520px;top:1100px;margin:0;text-align:center;
    font:600 30px/1.2 'Oswald',sans-serif;color:var(--white);text-transform:uppercase;}
  .call span{color:var(--maroon);}
  .email{position:absolute;left:0;width:520px;top:1148px;margin:0;text-align:center;
    font:700 17px/1.2 'Lato',sans-serif;color:var(--white);}
</style>
</head>
<body>
<main class="flyer">
  <div class="photo photo--hero" role="img" aria-label="Photo of white apartment blocks with balconies around a lawn and young trees"></div>
  <div class="photo photo--block-a" role="img" aria-label="Photo of a modern apartment facade with louvred screens"></div>
  <div class="photo photo--block-b" role="img" aria-label="Photo of a beige apartment building with flowering trees"></div>
  <div class="photo photo--block-c" role="img" aria-label="Photo of a brick and white apartment block with garden"></div>

  <svg class="shapes" viewBox="0 0 920 1200" aria-hidden="true">
    <defs>
      <linearGradient id="blueBand" x1="0" y1="0" x2="1" y2="0">
        <stop offset="0" stop-color="#0355a3"/>
        <stop offset="0.6" stop-color="#2a7bd0"/>
        <stop offset="1" stop-color="#0355a3"/>
      </linearGradient>
      <linearGradient id="paperFade" x1="0" y1="0" x2="0" y2="1">
        <stop offset="0" stop-color="#ffffff"/>
        <stop offset="1" stop-color="#e4e6ea"/>
      </linearGradient>
    </defs>

    <path d="M0 0H920V50H470V292C340 336 170 326 0 262Z" fill="var(--red)"/>
    <path d="M0 268C170 332 340 342 470 298" fill="none" stroke="#fff" stroke-width="7"/>
    <path d="M0 276C170 340 340 350 470 306V336C330 378 160 366 0 318Z" fill="url(#blueBand)"/>

    <path d="M0 660C200 735 380 700 511 640V1200H0Z" fill="url(#paperFade)"/>

    <path d="M0 596C260 686 560 616 920 494" fill="none" stroke="var(--red)" stroke-width="6"/>
    <path d="M0 604C260 694 560 624 920 502" fill="none" stroke="#fff" stroke-width="10"/>
    <path d="M0 612C260 702 560 632 920 510V534C580 660 260 740 0 664Z" fill="url(#blueBand)"/>
    <path d="M0 668C260 744 580 664 920 538" fill="none" stroke="#fff" stroke-width="8"/>

    <polygon points="37,746 165,688 165,724 511,724 511,768 165,768 165,804" fill="var(--red)"/>

    <line x1="44" y1="992" x2="474" y2="992" stroke="var(--red)" stroke-width="3"/>

    <path d="M0 1072C170 1028 390 1036 620 1160" fill="none" stroke="url(#blueBand)" stroke-width="16"/>
    <path d="M0 1086C170 1044 390 1052 620 1176" fill="none" stroke="#fff" stroke-width="10"/>
    <path d="M0 1094C170 1054 390 1062 620 1184V1200H0Z" fill="var(--red)"/>
  </svg>

  <p class="website">www.silverleafupkeepservices.com.au</p>

  <div class="brand">
    <div class="brand__dot"></div>
    <p class="brand__name">Silverleaf<br>Upkeep Services</p>
  </div>

  <h1 class="banner-title">Silverleaf Upkeep <span>Services</span></h1>

  <ul class="services services--left">
    <li>Building management</li>
    <li>Common area cleaning</li>
    <li>Window cleaning</li>
    <li>Lawn mowing</li>
  </ul>
  <ul class="services services--right">
    <li>Pressure cleaning</li>
    <li>Carpet cleaning</li>
    <li>Bin cleaning</li>
    <li>Handy man services</li>
    <li>Gardening</li>
  </ul>

  <p class="offer">Keep this flyer: 10% off your first service</p>

  <p class="tagline">Experience <span>Excellence</span></p>

  <p class="call"><span>Call us</span> 0438 507 721</p>
  <p class="email">Info@silverleafupkeepservices.com.au</p>
</main>
</body>
</html>
```